QDN Business Cards

I would like to use deep red (See attached logo), medium grays and white on the card to be used as separators for information using a white font over the red and gray colors. We are a web application design and development firm - specializing in custom software development with a content management solution. Our card needs to reflect innovative and cutting edge company.
I have attached the current card for content purposes - there is a front and back to the card. Open to suggestions on layout.

```html
<!DOCTYPE html>
<html lang="en">
<head>
<meta charset="utf-8">
<title>QDN Tech Group – Business Card</title>
<link href="https://fonts.googleapis.com/css2?family=Source+Sans+3:ital,wght@0,400;0,600;0,700;0,800;1,700;1,800&display=swap" rel="stylesheet">
<style>
  :root {
    --brand-red: #c8102e;
    --ink: #111111;
    --graphite: #3a3a3a;
    --paper: #ffffff;
    --font: "Source Sans 3", "Myriad Pro", Arial, sans-serif;
  }
  * { box-sizing: border-box; margin: 0; padding: 0; }
  html, body { width: 1045px; height: 1200px; overflow: hidden; background: var(--paper); }
  body { font-family: var(--font); }

  .sheet {
    position: relative;
    width: 1014px; height: 1162px;
    transform: scale(1.0306, 1.0327);
    transform-origin: 0 0;
  }
  .divider-band {
    position: absolute; left: 0; top: 540px;
    width: 1014px; height: 38px; background: var(--ink);
  }
  .card {
    position: absolute; left: 123px;
    width: 766px; overflow: hidden; background: var(--paper);
  }
  .card--front { top: 78px; height: 438px; }
  .card--back { top: 662px; height: 436px; }
  .card-shapes { position: absolute; inset: 0; width: 100%; height: 100%; }
  .shape-red { fill: var(--brand-red); }
  .shape-black { fill: var(--ink); }

  .abs { position: absolute; white-space: nowrap; }
  .centered { transform: translateX(-50%); text-align: center; }

  /* wordmark */
  .wordmark { color: var(--brand-red); font-weight: 700; line-height: 1; text-align: center; }
  .wordmark__name { display: block; letter-spacing: 4px; }
  .wordmark__sub { display: block; letter-spacing: 1px; }
  .card--front .wordmark { left: 40px; top: 30px; width: 380px; }
  .card--front .wordmark__name { font-size: 118px; }
  .card--front .wordmark__sub { font-size: 30px; margin-top: 8px; }
  .card--back .wordmark { left: 30px; top: 22px; width: 220px; }
  .card--back .wordmark__name { font-size: 72px; }
  .card--back .wordmark__sub { font-size: 19px; margin-top: 4px; }

  /* front details */
  .person-name { left: 655px; top: 34px; color: var(--paper); font-size: 27px; font-weight: 700; letter-spacing: .5px; }
  .person-title { left: 655px; top: 68px; color: var(--ink); font-size: 21px; font-weight: 800; }
  .address { left: 655px; top: 125px; color: var(--paper); font-size: 22px; font-weight: 600; line-height: 29.5px; }

  .tagline-arc { position: absolute; inset: 0; width: 100%; height: 100%; }
  .tagline-arc text { fill: var(--paper); font-family: var(--font); font-weight: 700; font-size: 24px; letter-spacing: .6px; }

  .contact { left: 273px; color: var(--ink); font-weight: 700; }
  .contact--phone { font-size: 16px; letter-spacing: .6px; }
  .contact--cell { top: 295px; }
  .contact--office { top: 320px; }
  .contact--fax { top: 345px; }
  .contact--email { top: 369px; color: var(--paper); font-size: 12.5px; }
  .contact--web { top: 395px; font-size: 16.5px; }

  /* back details */
  .follow { left: 752px; top: 52px; color: var(--paper); font-size: 12px; font-weight: 700; line-height: 15px; text-align: right; transform: translateX(-100%); }
  .follow__label { font-style: italic; display: block; }
  .follow__handle { display: block; }
  .social-slot {
    position: absolute; width: 48px; height: 48px;
    border-radius: 8px; background: var(--ink);
  }
  .social-slot--1 { left: 614px; top: 104px; }
  .social-slot--2 { left: 702px; top: 172px; }
  .social-slot--3 { left: 612px; top: 252px; }
  .social-slot--4 { left: 696px; top: 326px; border-radius: 50%; }

  .services {
    left: 327px; top: 188px;
    color: var(--paper); font-size: 28.5px; font-weight: 800; font-style: italic;
    line-height: 36.5px; letter-spacing: .2px;
  }
</style>
</head>
<body>
<main class="sheet">

  <!-- FRONT -->
  <section class="card card--front" aria-label="Card front">
    <svg class="card-shapes" viewBox="0 0 766 438" aria-hidden="true">
      <circle class="shape-black" cx="908" cy="240" r="463"/>
      <circle class="shape-red" cx="915" cy="240" r="449"/>
      <ellipse class="shape-black" cx="300" cy="470" rx="432" ry="274"/>
      <ellipse class="shape-red" cx="300" cy="478" rx="424" ry="262"/>
    </svg>

    <div class="wordmark abs">
      <span class="wordmark__name">QDN</span>
      <span class="wordmark__sub">TECH GROUP</span>
    </div>

    <svg class="tagline-arc" viewBox="0 0 766 438">
      <path id="tagline-path" d="M52 305 Q 272 198 495 305" fill="none"/>
      <text><textPath href="#tagline-path" startOffset="50%" text-anchor="middle">WOMAN OWNED SMALL BUSINESS</textPath></text>
    </svg>

    <p class="abs centered person-name">DANA MORROW</p>
    <p class="abs centered person-title">PRESIDENT</p>
    <p class="abs centered address">4820 Harbor View Pike<br>Suite 210<br>Millbrook, MD<br>20990</p>

    <p class="abs centered contact contact--phone contact--cell">C. 555.014.2290</p>
    <p class="abs centered contact contact--phone contact--office">O. 555.018.3471</p>
    <p class="abs centered contact contact--phone contact--fax">F. 555.016.5082</p>
    <p class="abs centered contact contact--email">DANA@QDNTECHGROUP.COM</p>
    <p class="abs centered contact contact--web">WWW.QDNTECHGROUP.COM</p>
  </section>

  <div class="divider-band" aria-hidden="true"></div>

  <!-- BACK -->
  <section class="card card--back" aria-label="Card back">
    <svg class="card-shapes" viewBox="0 0 766 436" aria-hidden="true">
      <ellipse class="shape-black" cx="330" cy="420" rx="440" ry="292"/>
      <ellipse class="shape-red" cx="330" cy="428" rx="432" ry="280"/>
      <circle class="shape-black" cx="950" cy="218" r="386"/>
      <circle class="shape-red" cx="956" cy="218" r="366"/>
    </svg>

    <div class="wordmark abs">
      <span class="wordmark__name">QDN</span>
      <span class="wordmark__sub">TECH GROUP</span>
    </div>

    <p class="abs follow"><span class="follow__label">FOLLOW US:</span><span class="follow__handle">@ QDNTECHGROUP</span></p>
    <span class="social-slot social-slot--1" role="img" aria-label="Social network icon"></span>
    <span class="social-slot social-slot--2" role="img" aria-label="Video channel icon"></span>
    <span class="social-slot social-slot--3" role="img" aria-label="Professional network icon"></span>
    <span class="social-slot social-slot--4" role="img" aria-label="Microblog icon"></span>

    <p class="abs centered services">PROJECT MGMT/STRATEGY,<br>WEB APP DEVELOPMENT,<br>MOBILE APP, DESIGN,<br>SECTION 508, TRAINING,<br>STAFFING, SOCIAL MEDIA<br>ADVERTISING &amp; MARKETING</p>
  </section>

</main>
</body>
</html>
```